電子書籍の表紙デザインを以下の内容で作成してください。 恋愛に関する書籍になりますが、 ビジネス書風のデザインをご希望されています。 恋愛を感じさせる要素は一切必要ありません。 ◆タイトル 朝が輝く習慣デザイン〜実践ガイド編〜 ◆サブタイトル 静けさは力に変わる ◆キャッチコピー ※帯デザインの部分に入れてほしいです。 ・モテない理由を徹底排除 ・髪・服・肌で人生を変える ・自分史上最大のモテ期になって、理想の彼女からオファーされる ・アプリで出会えても交際に発展しない。狙っている本命ほど、2回目のデートに繋がらない。そもそも可愛い彼女に申し込んでもらえない人必見! ◆お願い 吹き出しみたいな感じで 「ビジネスにも使える」と入れてください。 ◆著者名 サヤカ ◆肩書き 瞬間モテ構築のプロ ◆出版社名 Lumeria出版 ◆その他 ・白背景で、必ず枠線を入れてください。 ・帯デザインを入れて、その部分に文字を入れてください。 ・文字の色は、黒、グレーなどシンプルにお願いします。 ・アクセントカラーとして赤(#9c2020)を入れてください。 ・全体のデザインは、以下のようなイメージです。 https://www.novashelf.example/dp/X7Q2LM8R4K https://www.novashelf.example/dp/9315064827 ◆注意事項 Pagelo セルフ・リリースの表紙画像の要件を満たすように作成をお願いします。 https://publish.novashelf.example/ja_JP/help/topic/H418273095 どうぞよろしくお願いいたします。 |
どの案も素敵でしたが、
著者様のイメージがこちらのデザインでした。
みなさま、ご提案ありがとうございました。
どれも目立つデザインで素晴らしかったです。
今後も、電子書籍の表紙デザインや
本文に挿入するイラストなどの依頼をするので、

```html
<!DOCTYPE html>
<html lang="ja">
<head>
<meta charset="utf-8">
<title>朝が輝く習慣デザイン〜実践ガイド編〜</title>
<link rel="stylesheet" href="https://fonts.googleapis.com/css2?family=Noto+Serif+JP:wght@500;700;900&family=Noto+Sans+JP:wght@400;500;700;900&display=swap">
<style>
  :root {
    --ink: #1c1c1c;
    --gray: #7d7d7d;
    --gray-light: #b5b5b5;
    --band: #f0f0f0;
    --accent: #9c2020;
    --paper: #ffffff;
  }
  * { margin: 0; padding: 0; box-sizing: border-box; }
  html, body { width: 749px; height: 1200px; overflow: hidden; background: var(--paper); }
  .cover {
    position: relative; width: 749px; height: 1200px; background: var(--paper);
    font-family: "Noto Sans JP", sans-serif; color: var(--ink);
  }
  .frame { position: absolute; inset: 22px; border: 2px solid var(--gray-light); }
  .publisher {
    position: absolute; top: 30px; left: 0; width: 100%; text-align: center;
    font-size: 26px; font-weight: 500; letter-spacing: 1px;
  }
  .title { font-family: "Noto Serif JP", serif; font-weight: 900; position: absolute; line-height: 1; white-space: nowrap; }
  .title-top { top: 70px; left: 96px; font-size: 92px; letter-spacing: 28px; }
  .title-main { top: 182px; left: 116px; font-size: 160px; letter-spacing: 18px; }
  .title-bottom { top: 372px; left: 96px; font-size: 100px; letter-spacing: 28px; }
  .edition {
    position: absolute; top: 492px; left: 60px; width: 520px; text-align: center;
    font-size: 30px; font-weight: 500; color: var(--accent); letter-spacing: 6px;
  }
  .subtitle {
    position: absolute; top: 542px; left: 60px; width: 520px; text-align: center;
    font-family: "Noto Serif JP", serif; font-size: 30px; font-weight: 700; color: var(--accent); letter-spacing: 10px;
  }
  .author-role {
    position: absolute; top: 166px; left: 556px; writing-mode: vertical-rl;
    font-size: 17px; font-weight: 700; color: var(--accent); letter-spacing: 2px;
    border: 1.5px solid var(--accent); padding: 6px 3px;
  }
  .author-name {
    position: absolute; top: 164px; left: 596px; writing-mode: vertical-rl;
    font-size: 54px; font-weight: 900; color: var(--accent); letter-spacing: 6px; line-height: 1;
  }
  .author-name small { font-size: 30px; font-weight: 700; color: var(--ink); margin-top: 10px; }
  .badge { position: absolute; top: 450px; left: 586px; width: 140px; height: 140px; }
  .badge-text {
    position: absolute; top: 470px; left: 598px; width: 120px; transform: rotate(-14deg);
    text-align: center; color: #fff; font-weight: 900; font-size: 24px; line-height: 1.2;
  }
  .obi {
    position: absolute; left: 24px; right: 24px; top: 618px; bottom: 24px;
    background: var(--band); border-top: 6px solid var(--gray-light);
  }
  .obi-lead {
    position: absolute; top: 654px; left: 46px; width: 500px; height: 78px;
    border: 3px solid var(--gray-light); border-radius: 8px; background: var(--paper);
    display: flex; align-items: center; justify-content: center;
    font-size: 42px; font-weight: 900; color: var(--gray); letter-spacing: 2px;
  }
  .obi-head { position: absolute; top: 756px; left: 46px; font-weight: 900; white-space: nowrap; }
  .obi-head .big { font-size: 54px; }
  .obi-head .rest { font-size: 42px; }
  .obi-offer { position: absolute; left: 46px; top: 858px; }
  .obi-offer p {
    display: inline-block; background: var(--paper); border: 1.5px solid var(--gray-light);
    font-size: 30px; font-weight: 700; padding: 2px 10px; margin-bottom: 10px; letter-spacing: 1px;
  }
  .obi-offer em { font-style: normal; color: var(--accent); }
  .obi-vertical {
    position: absolute; top: 648px; writing-mode: vertical-rl;
    font-size: 42px; font-weight: 900; letter-spacing: 4px; line-height: 1;
  }
  .obi-vertical.first { left: 694px; }
  .obi-vertical.second { left: 648px; letter-spacing: 2px; }
  .obi-vertical .strong { font-size: 46px; }
  .must-read {
    position: absolute; top: 880px; left: 534px; writing-mode: vertical-rl;
    font-family: "Noto Serif JP", serif; font-size: 108px; font-weight: 900; line-height: 1;
  }
  .obi-problem { position: absolute; left: 46px; top: 998px; }
  .obi-problem .note { font-size: 23px; font-weight: 500; color: var(--gray); margin-bottom: 16px; letter-spacing: 1px; }
  .obi-problem .line {
    font-size: 31px; font-weight: 700; color: var(--gray); letter-spacing: 2px;
    border-bottom: 2px solid var(--gray-light); padding-bottom: 4px; margin-bottom: 12px; width: 478px;
  }
</style>
</head>
<body>
<div class="cover">
  <div class="frame"></div>
  <div class="publisher">Lumeria出版</div>

  <h1 class="title-block">
    <span class="title title-top">朝が輝く</span>
    <span class="title title-main">習慣</span>
    <span class="title title-bottom">デザイン</span>
  </h1>
  <div class="edition">— 実践ガイド編 —</div>
  <div class="subtitle">静けさは力に変わる</div>

  <div class="author-role">瞬間モテ構築のプロ</div>
  <div class="author-name">サヤカ<small>著</small></div>

  <svg class="badge" viewBox="0 0 140 140" aria-hidden="true">
    <path d="M30 108 L6 132 L44 116 Z" fill="var(--accent)"/>
    <circle cx="76" cy="66" r="62" fill="var(--accent)"/>
  </svg>
  <div class="badge-text">ビジネス<br>にも<br>使える</div>

  <div class="obi"></div>
  <div class="obi-lead">モテない理由を徹底排除</div>
  <div class="obi-head"><span class="big">髪・服・肌</span><span class="rest">で人生を変える</span></div>
  <div class="obi-offer">
    <p>自分史上<em>最大</em>のモテ期になって、</p><br>
    <p>理想の彼女からオファーされる</p>
  </div>

  <div class="obi-vertical first">そもそも<span class="strong">可愛い彼女に</span></div>
  <div class="obi-vertical second">申し込んでもらえない人</div>
  <div class="must-read">必見</div>

  <div class="obi-problem">
    <p class="note">アプリで出会えても交際に発展しない。</p>
    <p class="line">狙っている本命ほど、</p>
    <p class="line">2回目のデートに繋がらない。</p>
  </div>
</div>
</body>
</html>
```